Business card design needed

I need a business card design for a dog walking, dog minding and dog training business. Please refer to my website for the basic company colours and fonts I'm after. Planning on a double sided card, so all information doesn't need to be on the 'front' side.
Cheers

Industry/Entity Type

Dog Training

Contact Information for Business Card

Meadow Paws - happy hounds
Rua 0498307164
meadowpawsdemo.com.au
-walking
-holiday stays
-onsite care
-training and behavioural consultations

```html
<!DOCTYPE html>
<html lang="en">
<head>
<meta charset="utf-8">
<title>Meadow Paws – Business Card</title>
<link href="https://fonts.googleapis.com/css2?family=Source+Sans+3:wght@400;600&display=swap" rel="stylesheet">
<style>
  :root {
    --card-bg: #333333;
    --bone-orange: #c9500f;
    --bone-edge: #ffffff;
    --text-light: #ffffff;
    --text-dark: #2b2b2b;
  }
  html, body {
    margin: 0;
    padding: 0;
    overflow: hidden;
    background: var(--card-bg);
  }
  .card {
    position: relative;
    width: 1200px;
    height: 693px;
    background: var(--card-bg);
    overflow: hidden;
    font-family: "Source Sans 3", "Myriad Pro", sans-serif;
    color: var(--text-light);
  }
  .bone-art {
    position: absolute;
    left: 0;
    top: 0;
  }
  .contact {
    position: absolute;
    left: 360px;
    top: 76px;
    display: flex;
    flex-direction: column;
    gap: 22px;
  }
  .contact-row {
    display: flex;
    align-items: center;
    gap: 36px;
    font-size: 42px;
    line-height: 1;
    letter-spacing: 1px;
  }
  .contact-icon {
    width: 44px;
    height: 44px;
    flex: none;
  }
  .brand {
    position: absolute;
    left: 0;
    width: 1200px;
    top: 262px;
    text-align: center;
  }
  .brand-name {
    margin: 0;
    font-weight: 600;
    font-size: 74px;
    letter-spacing: 4px;
    text-transform: uppercase;
    line-height: 1;
    color: var(--text-light);
  }
  .brand-tagline {
    margin: 14px 0 0;
    font-weight: 400;
    font-size: 34px;
    letter-spacing: 2px;
    color: var(--text-light);
  }
  .services {
    position: absolute;
    left: 0;
    width: 1240px;
    top: 494px;
    margin: 0;
    text-align: center;
    font-size: 39px;
    line-height: 51px;
  }
</style>
</head>
<body>
<main class="card">
  <svg class="bone-art" width="1200" height="693" viewBox="0 0 1200 693" role="img" aria-label="Large orange dog bone illustration outlined in white, spanning the card">
    <rect x="70" y="48" width="1072" height="620" rx="120" fill="var(--bone-orange)" stroke="var(--bone-edge)" stroke-width="10"/>
  </svg>

  <div class="contact">
    <div class="contact-row">
      <svg class="contact-icon" viewBox="0 0 44 44" aria-hidden="true">
        <rect x="1.5" y="1.5" width="41" height="41" rx="6" fill="none" stroke="#fff" stroke-width="3"/>
        <path d="M8 23 L22 10 L36 23" fill="none" stroke="#fff" stroke-width="3.5" stroke-linejoin="round"/>
        <path d="M13 22 V35 H19 V27 H25 V35 H31 V22" fill="#fff"/>
      </svg>
      <span class="contact-text">meadowpawsdemo.com.au</span>
    </div>
    <div class="contact-row">
      <svg class="contact-icon" viewBox="0 0 44 44" aria-hidden="true">
        <rect x="1.5" y="1.5" width="41" height="41" rx="6" fill="none" stroke="#fff" stroke-width="3"/>
        <path d="M16 8 h7 v8 h-4 q-2 6 0 12 h4 v8 h-7 q-6 -14 0 -28 z" fill="none" stroke="#fff" stroke-width="2.5" stroke-linejoin="round"/>
      </svg>
      <span class="contact-text">Rua 0498 307 164</span>
    </div>
  </div>

  <div class="brand">
    <h1 class="brand-name">Meadow Paws</h1>
    <p class="brand-tagline">happy hounds</p>
  </div>

  <p class="services">Walking, Holiday stays,<br>Onsite care, Training and<br>Behavioural consultations</p>
</main>
</body>
</html>
```